Business card and stationery
Clear Harbour
Project: Business card and stationery
Business card and stationery  -
Creative Brief
Simple
Name Surname
Executive Director
317 Larkmoor Lane, #03 Fenwick Plaza, Country 264519
vantolemu@mailpost.example
www.clearharbour.example.sg
info (name, address, email etc) on the card should be editable for each employee

```html
<!DOCTYPE html>
<html lang="en">
<head>
<meta charset="utf-8">
<title>Clear Harbour — Business Card</title>
<link href="https://fonts.googleapis.com/css2?family=Open+Sans:wght@400;600;700&display=swap" rel="stylesheet">
<style>
  :root {
    --bg: #e9e4dc;
    --card: #ffffff;
    --brand-blue: #2d74dc;
    --brand-green: #3fb62a;
    --ink: #333a44;
    --white: #ffffff;
  }
  * { margin: 0; padding: 0; box-sizing: border-box; }
  html, body { width: 1200px; height: 581px; overflow: hidden; }
  body {
    background: var(--bg);
    font-family: "Open Sans", Arial, sans-serif;
    position: relative;
  }
  .card {
    position: absolute;
    top: 149px;
    width: 487px;
    height: 283px;
    border-radius: 16px;
    background: var(--card);
    overflow: hidden;
    box-shadow: 0 3px 10px rgba(0,0,0,0.18);
  }
  .card--front { left: 96px; }
  .card--back { left: 607px; }
  .card__bands { position: absolute; inset: 0; }

  .person { position: absolute; left: 22px; top: 24px; color: var(--white); }
  .person__name { font-size: 20px; font-weight: 700; line-height: 1.1; }
  .person__title { font-size: 10px; font-weight: 600; margin-top: 3px; }

  .contact { position: absolute; left: 22px; top: 132px; color: var(--white); font-size: 10.5px; line-height: 1.4; }
  .contact__address { margin-bottom: 8px; }
  .contact__row { display: flex; align-items: center; gap: 6px; line-height: 1.55; }
  .contact__icon { width: 11px; height: 11px; flex: none; }

  .brand { position: absolute; display: flex; flex-direction: column; align-items: center; }
  .brand__mark { width: 36px; height: 36px; border-radius: 50%; background: var(--brand-green); }
  .brand__name { color: var(--brand-blue); font-weight: 700; white-space: nowrap; margin-top: 6px; }
  .card--front .brand { left: 290px; top: 84px; width: 185px; }
  .card--front .brand__name { font-size: 23px; }
  .card--back .brand { left: 0; right: 0; top: 78px; }
  .card--back .brand__mark { width: 42px; height: 42px; }
  .card--back .brand__name { font-size: 28px; }

  .website { position: absolute; left: 0; right: 0; bottom: 38px; text-align: center; color: var(--ink); font-size: 15px; font-weight: 600; }
</style>
</head>
<body>
  <section class="card card--front">
    <svg class="card__bands" viewBox="0 0 487 283" preserveAspectRatio="none">
      <path d="M0 0 H226 C252 50 250 190 392 283 H0 Z" fill="var(--brand-green)"/>
      <path d="M0 0 H210 C236 50 234 190 372 283 H0 Z" fill="var(--brand-blue)"/>
    </svg>
    <div class="person">
      <div class="person__name">Name Surname</div>
      <div class="person__title">Executive Director</div>
    </div>
    <div class="contact">
      <div class="contact__address">317 Larkmoor Lane,<br>#03 Fenwick Plaza,<br>Country 264519</div>
      <div class="contact__row">
        <svg class="contact__icon" viewBox="0 0 12 12"><path d="M2.5 1 L4.5 1 L5.2 3.5 L4 4.6 C4.7 6 6 7.3 7.4 8 L8.5 6.8 L11 7.5 L11 9.5 C11 10.4 10.3 11 9.5 11 C5 11 1 7 1 2.5 C1 1.7 1.6 1 2.5 1 Z" fill="var(--white)"/></svg>
        <span>+65 6100 2040</span>
      </div>
      <div class="contact__row">
        <svg class="contact__icon" viewBox="0 0 12 12"><rect x="3" y="0.5" width="6" height="11" rx="1.2" fill="var(--white)"/><rect x="4" y="2" width="4" height="6.5" fill="var(--brand-blue)"/></svg>
        <span>+65 9300 4180</span>
      </div>
      <div class="contact__row">
        <svg class="contact__icon" viewBox="0 0 12 12"><circle cx="6" cy="6" r="5.5" fill="var(--white)"/><rect x="3" y="4" width="6" height="4.2" fill="none" stroke="var(--brand-blue)" stroke-width="0.9"/><path d="M3 4 L6 6.4 L9 4" fill="none" stroke="var(--brand-blue)" stroke-width="0.9"/></svg>
        <span>vantolemu@mailpost.example</span>
      </div>
      <div class="contact__row">
        <svg class="contact__icon" viewBox="0 0 12 12"><circle cx="6" cy="6" r="5.5" fill="var(--white)"/><circle cx="6" cy="6" r="3.6" fill="none" stroke="var(--brand-blue)" stroke-width="0.8"/><ellipse cx="6" cy="6" rx="1.6" ry="3.6" fill="none" stroke="var(--brand-blue)" stroke-width="0.8"/><path d="M2.4 6 H9.6" stroke="var(--brand-blue)" stroke-width="0.8"/></svg>
        <span>www.clearharbour.example.sg</span>
      </div>
    </div>
    <div class="brand">
      <div class="brand__mark"></div>
      <div class="brand__name">Clear Harbour</div>
    </div>
  </section>

  <section class="card card--back">
    <div class="brand">
      <div class="brand__mark"></div>
      <div class="brand__name">Clear Harbour</div>
    </div>
    <div class="website">www.clearharbour.example.sg</div>
  </section>
</body>
</html>
```